Vellora - Quality health delivered at your door

Vellora offers home and Community Based Services for adults who wish to continue live independently in their communities. We increase accessibility to health care, reduce health care delivery gap, reduce mortality and morbidity, reduce health while promoting healthy living in the comfort of our patients communities or homes.

We provide on site services and deliver high quality healthcare at your door. Our experienced physicians coordinate care with our certified nurse practitioners and provide chronic care management, physical therapy, rehabilitation and medications management.

Target Market(s)

Older population living in independent living facilities

Industry/Entity Type

Health Care

Contact Information for Business Card

Vellora

Number of Pages Required

4 page

Font styles to use
Sans Serif

Colors

Designer to choose colors to be used in the design.

```html
<!DOCTYPE html>
<html lang="en">
<head>
<meta charset="utf-8">
<title>Vellora - Quality health delivered at your door</title>
<link href="https://fonts.googleapis.com/css2?family=Lato:wght@400;700;900&display=swap" rel="stylesheet">
<style>
:root{
  --orange:#f7941d;
  --orange-soft:rgba(247,148,29,.9);
  --green:#4d7000;
  --ink:#5a5e62;
  --heading:#5b5f63;
  --grey-bg:#eeeef1;
  --white:#fff;
}
*{margin:0;padding:0;box-sizing:border-box}
html,body{width:1200px;height:2687px;overflow:hidden}
body{font-family:'Lato',Arial,sans-serif;background:var(--white);position:relative;color:var(--ink)}
.abs{position:absolute}

/* header */
.site-header{top:0;left:0;width:1200px;height:140px;background:var(--white)}
.brand{left:124px;top:14px;width:170px;text-align:center}
.brand-mark{width:78px;height:78px;border-radius:50%;background:var(--orange);border:5px solid var(--green);margin:0 auto}
.brand-name{font-size:23px;font-weight:400;color:#1f3300;letter-spacing:.5px;margin-top:8px;line-height:1}
.top-btn{top:21px;height:25px;font-size:10px;font-weight:700;display:flex;align-items:center;justify-content:center;text-transform:uppercase}
.top-btn.home{left:867px;width:59px;background:var(--orange);color:var(--white)}
.top-btn.learning{left:938px;width:115px;border:1px solid #c9c9c9;color:#777}
.call-icon{left:867px;top:73px;width:38px;height:38px;border:2px solid var(--orange);border-radius:50%;display:flex;align-items:center;justify-content:center}
.call-label{left:921px;top:70px;font-size:10px;font-weight:700;color:#333}
.call-number{left:919px;top:86px;font-size:24px;color:var(--orange);font-weight:400}

/* nav */
.main-nav{top:140px;left:0;width:1200px;height:34px;background:var(--green);display:flex;justify-content:center;align-items:center;gap:30px}
.main-nav a{color:var(--white);font-size:10px;font-weight:700;text-decoration:none;text-transform:uppercase;letter-spacing:.2px}

/* hero */
.hero{top:174px;left:0;width:1200px;height:530px;
  background:
    radial-gradient(ellipse 120px 260px at 690px 420px,rgba(58,170,150,.85),rgba(58,170,150,0)),
    radial-gradient(ellipse 150px 300px at 1000px 420px,rgba(110,110,100,.8),rgba(110,110,100,0)),
    radial-gradient(ellipse 90px 80px at 950px 80px,rgba(236,232,226,.95),rgba(236,232,226,0)),
    radial-gradient(ellipse 70px 70px at 725px 120px,rgba(235,210,180,.8),rgba(235,210,180,0)),
    radial-gradient(ellipse 280px 140px at 500px 130px,rgba(140,80,40,.75),rgba(140,80,40,0)),
    radial-gradient(ellipse 420px 260px at 160px 220px,rgba(120,160,50,.9),rgba(120,160,50,0)),
    radial-gradient(ellipse 600px 160px at 500px 520px,rgba(170,150,110,.6),rgba(170,150,110,0)),
    linear-gradient(180deg,#dfe9b8 0%,#a9c870 45%,#8aa84a 100%);}
.hero-badge{left:143px;top:365px;width:299px;height:162px;background:var(--orange-soft);padding:20px 22px}
.hero-badge h1{color:var(--white);font-size:31px;font-weight:900;line-height:1.3;text-transform:uppercase}
.hero-dots{left:561px;top:657px;display:flex;gap:7px}
.hero-dots span{width:11px;height:11px;border-radius:50%;background:#555;border:2px solid #fff}
.hero-dots span.on{background:#fff}

/* welcome */
.welcome-photo{left:133px;top:783px;width:453px;height:292px;
  background:
    radial-gradient(ellipse 60px 90px at 180px 170px,rgba(150,150,150,.85),rgba(150,150,150,0)),
    radial-gradient(ellipse 45px 100px at 270px 160px,rgba(120,110,95,.8),rgba(120,110,95,0)),
    radial-gradient(ellipse 260px 90px at 220px 50px,rgba(60,90,30,.9),rgba(60,90,30,0)),
    linear-gradient(180deg,#5f8530 0%,#86a846 40%,#a6c35a 60%,#b9cf6c 100%);}
.welcome-seal{left:487px;top:754px;width:126px;height:126px;border-radius:50%;background:var(--orange);border:9px solid var(--green);box-shadow:0 0 0 5px var(--white)}
.welcome-title{left:647px;top:784px;font-size:24px;font-weight:900;color:var(--orange);text-transform:uppercase}
.rule{height:2px;background:var(--orange)}
.welcome-rule{left:647px;top:823px;width:115px}
.welcome-copy{left:647px;top:842px;width:415px;font-size:13.6px;line-height:1.5;text-align:justify;color:var(--ink)}
.welcome-copy p+p{margin-top:18px}
.btn{display:flex;align-items:center;justify-content:center;background:var(--green);color:var(--white);font-size:11px;font-weight:700;text-transform:uppercase}
.read-more{left:647px;top:1044px;width:116px;height:34px}

/* services */
.services{top:1143px;left:0;width:1200px;height:705px;background:var(--grey-bg)}
.services-title{top:1192px;left:0;width:1200px;text-align:center;font-size:24px;font-weight:900;color:var(--orange)}
.services-rule{left:579px;top:1234px;width:42px}
.service-card{width:301px;height:202px;display:flex;align-items:flex-end}
.service-card span{display:block;width:100%;height:32px;background:var(--orange-soft);color:var(--white);font-size:16px;font-weight:700;padding:6px 10px}
.tile-social{background:
  radial-gradient(ellipse 90px 110px at 100px 110px,rgba(40,80,150,.85),rgba(40,80,150,0)),
  radial-gradient(ellipse 70px 90px at 220px 120px,rgba(60,180,200,.75),rgba(60,180,200,0)),
  linear-gradient(135deg,#e2d6c2,#c9c0b0)}
.tile-home{background:
  radial-gradient(ellipse 120px 25px at 150px 50px,rgba(225,160,90,.8),rgba(225,160,90,0)),
  radial-gradient(ellipse 110px 90px at 150px 130px,rgba(150,150,160,.6),rgba(150,150,160,0)),
  linear-gradient(135deg,#eceae7,#c9c4bf)}
.tile-therapy{background:
  radial-gradient(ellipse 70px 80px at 220px 110px,rgba(120,160,210,.8),rgba(120,160,210,0)),
  radial-gradient(ellipse 60px 70px at 90px 120px,rgba(225,110,130,.6),rgba(225,110,130,0)),
  linear-gradient(135deg,#f2f0f0,#d8dde3)}
.tile-mental{background:
  radial-gradient(ellipse 60px 90px at 100px 120px,rgba(150,150,155,.75),rgba(150,150,155,0)),
  radial-gradient(ellipse 60px 80px at 230px 120px,rgba(225,200,150,.8),rgba(225,200,150,0)),
  linear-gradient(135deg,#eeebe5,#d6cfc4)}
.tile-dental{background:
  radial-gradient(ellipse 110px 100px at 110px 100px,rgba(230,180,150,.85),rgba(230,180,150,0)),
  radial-gradient(ellipse 80px 100px at 260px 80px,rgba(90,140,200,.8),rgba(90,140,200,0)),
  linear-gradient(135deg,#e6d6c8,#a9c1d6)}
.tile-nursing{background:
  radial-gradient(ellipse 80px 80px at 90px 130px,rgba(230,100,150,.8),rgba(230,100,150,0)),
  radial-gradient(ellipse 70px 100px at 250px 110px,rgba(40,130,160,.85),rgba(40,130,160,0)),
  linear-gradient(135deg,#ddd6cf,#9fb5be)}
.view-all{left:518px;top:1764px;width:166px;height:36px}

/* cta */
.cta{top:1848px;left:0;width:1200px;height:468px;
  background:
    radial-gradient(ellipse 180px 170px at 800px 190px,rgba(225,205,190,.9),rgba(225,205,190,0)),
    radial-gradient(ellipse 230px 150px at 790px 110px,rgba(245,245,245,.95),rgba(245,245,245,0)),
    radial-gradient(ellipse 380px 160px at 780px 420px,rgba(120,200,210,.9),rgba(120,200,210,0)),
    radial-gradient(ellipse 200px 200px at 1130px 260px,rgba(235,238,240,.9),rgba(235,238,240,0)),
    linear-gradient(90deg,#eef1f3 0%,#e2e7ea 40%,#d4dee2 65%,#c7dadf 100%);}
.cta-text{left:145px;top:1962px;width:440px;font-size:27px;font-weight:700;line-height:1.33;color:var(--heading)}
.contact-btn{left:149px;top:2092px;width:150px;height:41px;background:var(--orange);font-size:14px}

/* footer */
.site-footer{top:2316px;left:0;width:1200px;height:371px;background:var(--green)}
.footer-seal{left:546px;top:2278px;width:108px;height:108px;border-radius:50%;background:var(--orange);border:8px solid var(--green);box-shadow:0 0 0 4px var(--white)}
.footer-name{top:2384px;left:0;width:1200px;text-align:center;font-size:25px;color:#1d2a05}
.follow{top:2437px;left:0;width:1200px;display:flex;justify-content:center;align-items:center;gap:16px;color:var(--white);font-size:11px;letter-spacing:3px}
.follow i{display:block;width:28px;height:1px;background:rgba(255,255,255,.6)}
.social{top:2477px;left:0;width:1200px;display:flex;justify-content:center;gap:17px}
.social span{width:28px;height:28px;border-radius:50%;background:var(--orange)}
.footer-links{top:2541px;left:0;width:1200px;text-align:center;color:var(--white);font-size:11px;line-height:24px}
.copyright{top:2628px;left:0;width:1200px;text-align:center;color:var(--white);font-size:10px}
</style>
</head>
<body>

<header class="site-header abs">
  <div class="brand abs">
    <div class="brand-mark"></div>
    <div class="brand-name">VELLORA</div>
  </div>
  <div class="top-btn home abs">Home</div>
  <div class="top-btn learning abs">Kestra Learning®</div>
  <div class="call-icon abs">
    <svg width="18" height="18" viewBox="0 0 24 24"><path d="M6.6 10.8a15.1 15.1 0 0 0 6.6 6.6l2.2-2.2a1 1 0 0 1 1-.25 11.4 11.4 0 0 0 3.6.57 1 1 0 0 1 1 1V20a1 1 0 0 1-1 1A17 17 0 0 1 3 4a1 1 0 0 1 1-1h3.5a1 1 0 0 1 1 1c0 1.25.2 2.45.57 3.57a1 1 0 0 1-.25 1z" fill="#f7941d"/></svg>
  </div>
  <div class="call-label abs">CALL US NOW</div>
  <div class="call-number abs">555.014.2290</div>
</header>

<nav class="main-nav abs">
  <a>Assisted Living</a><a>Skilled Nursing</a><a>Independent Living</a><a>Home and Community Based Services</a><a>Respite Care</a><a>Rehabilitation</a><a>Kestra Learning Center</a>
</nav>

<section class="hero abs" role="img" aria-label="Photo: a smiling nurse in teal scrubs helping an older man with a walker outdoors beside a wooden gazebo"></section>
<div class="hero-badge abs"><h1>High quality healthcare at your door</h1></div>
<div class="hero-dots abs"><span></span><span class="on"></span><span></span><span></span><span></span></div>

<div class="welcome-photo abs" role="img" aria-label="Photo: a caregiver holding hands with an older man in a wheelchair on a sunny lawn"></div>
<div class="welcome-seal abs"></div>
<h2 class="welcome-title abs">Welcome to our site</h2>
<div class="rule welcome-rule abs"></div>
<div class="welcome-copy abs">
  <p>Vellora offers home and Community Based Services for adults who wish to continue to live independently in the comfort of their communities.</p>
  <p>We provide on site services and deliver high quality healthcare at your door. Our experienced physicians coordinate care with our certified nurse practitioners and provide chronic care management, physical therapy, rehabilitation and medications management.</p>
</div>
<div class="btn read-more abs">Read more</div>

<section class="services abs"></section>
<h2 class="services-title abs">OUR SERVICES</h2>
<div class="rule services-rule abs"></div>
<div class="service-card tile-social abs" style="left:131px;top:1290px" role="img" aria-label="Photo: a carer hugging an older woman"><span>Social services assessment</span></div>
<div class="service-card tile-home abs" style="left:450px;top:1290px" role="img" aria-label="Photo: an older couple exercising with a resistance band"><span>Home health assistance</span></div>
<div class="service-card tile-therapy abs" style="left:768px;top:1290px" role="img" aria-label="Photo: a therapist guiding an older woman through arm exercises"><span>Physical therapy</span></div>
<div class="service-card tile-mental abs" style="left:131px;top:1512px" role="img" aria-label="Photo: a counsellor talking with a client"><span>Mental health</span></div>
<div class="service-card tile-dental abs" style="left:450px;top:1512px" role="img" aria-label="Photo: a patient smiling during a dental check-up"><span>Dental health</span></div>
<div class="service-card tile-nursing abs" style="left:768px;top:1512px" role="img" aria-label="Photo: a nurse checking an older woman's blood pressure"><span>Skilled nursing visits</span></div>
<div class="btn view-all abs">View all services</div>

<section class="cta abs" role="img" aria-label="Photo: a happy older woman with white hair in a light blue cardigan"></section>
<p class="cta-text abs">Our experienced physicians coordinate care with our certified nurse practitioners</p>
<div class="btn contact-btn abs">Contact us</div>

<footer class="site-footer abs"></footer>
<div class="footer-seal abs"></div>
<div class="footer-name abs">VELLORA</div>
<div class="follow abs"><i></i>FOLLOW US<i></i></div>
<div class="social abs"><span></span><span></span><span></span><span></span></div>
<div class="footer-links abs">
  Assisted Living &nbsp;|&nbsp; Skilled Nursing &nbsp;|&nbsp; Independent Living &nbsp;|&nbsp; Home and Community Based Services &nbsp;|&nbsp; Respite Care<br>
  Rehabilitation &nbsp;|&nbsp; Kestra Learning Center &nbsp;|&nbsp; Kestra Learning®
</div>
<div class="copyright abs">Copyrights @ 2017 All Rights Reserved</div>

</body>
</html>
```